Elegant Black Candle Label Design!

I need a 2.375" tall by 3.0" wide candle label design. I'm looking for simple and elegant. Black label with silver leaf border and lettering. Label needs to have the following information on it: Fern Hollow Candle Co. as the company name, scent name in the middle and in smaller font, it needs to say Made in USA, All Natural, 8oz. Attached photos are for inspiration.

Target Market(s)

People looking for high end, all natural candle fragrances

Industry/Entity Type

Candle-Spa

Colors

Designer to choose only greyscale colors for use in the design.

Requirements
Must have
• Company Name, Scent (ability to change scent names), All Natural, Made in USA, 8oz
Nice to have
• Black background, silver leaf border and silver leaf font. Elegant fonts maybe slightly cursive

```html
<!DOCTYPE html>
<html lang="en">
<head>
<meta charset="UTF-8">
<title>Fern Hollow Candle Co. — Cherry Blossom Label</title>
<link href="https://fonts.googleapis.com/css2?family=Montserrat:wght@300;400;700&family=Mr+Dafoe&display=swap" rel="stylesheet">
<style>
  :root {
    --backdrop: #b4b4b4;
    --label-black: #060606;
    --silver-light: #f2f2f2;
    --silver-mid: #a9a9a9;
    --silver-dark: #5a5a5a;
    --ink-white: #ffffff;
  }
  * { margin: 0; padding: 0; box-sizing: border-box; }
  html, body {
    width: 1099px;
    height: 1200px;
    overflow: hidden;
    background: var(--backdrop);
  }
  .canvas {
    position: relative;
    width: 1099px;
    height: 1200px;
    display: flex;
    align-items: center;
    justify-content: center;
  }
  .label {
    position: relative;
    width: 900px;
    height: 712px;
    padding: 12px;
    background: linear-gradient(90deg,
      var(--silver-dark) 0%, var(--silver-light) 8%, var(--silver-mid) 25%,
      var(--silver-light) 50%, var(--silver-mid) 72%, var(--silver-light) 92%,
      var(--silver-dark) 100%);
  }
  .label-face {
    position: relative;
    width: 100%;
    height: 100%;
    background: linear-gradient(90deg, var(--label-black) 0%, var(--label-black) 65%, #222 82%, var(--label-black) 100%);
    display: flex;
    flex-direction: column;
    align-items: center;
    color: var(--ink-white);
  }
  .brand-name {
    margin-top: 92px;
    font-family: 'Montserrat', sans-serif;
    font-weight: 300;
    font-size: 44px;
    letter-spacing: 2px;
    color: var(--silver-light);
  }
  .scent-name {
    margin-top: 100px;
    font-family: 'Mr Dafoe', cursive;
    font-size: 118px;
    line-height: 1;
    color: var(--ink-white);
  }
  .divider {
    margin-top: 118px;
    width: 430px;
    height: 3px;
    background: linear-gradient(90deg, var(--silver-dark), var(--silver-light) 30%, var(--silver-mid) 60%, var(--silver-light) 85%, var(--silver-dark));
  }
  .claims {
    margin-top: 46px;
    font-family: 'Montserrat', sans-serif;
    font-weight: 400;
    font-size: 22px;
    letter-spacing: 3.5px;
    color: var(--silver-light);
  }
  .claims strong { font-weight: 700; }
  .claims .separator { margin: 0 14px; }
  .net-weight {
    margin-top: 30px;
    font-family: 'Montserrat', sans-serif;
    font-weight: 400;
    font-size: 40px;
    color: var(--ink-white);
  }
  .net-weight .unit { font-size: 24px; }
</style>
</head>
<body>
  <main class="canvas">
    <section class="label">
      <div class="label-face">
        <h1 class="brand-name">Fern Hollow Candle Co.</h1>
        <h2 class="scent-name">cherry blossom</h2>
        <div class="divider"></div>
        <p class="claims">Made in <strong>USA</strong><span class="separator">|</span>All Natural</p>
        <p class="net-weight">8<span class="unit">oz</span></p>
      </div>
    </section>
  </main>
</body>
</html>
```